I am a new company with the latest technology in the concrete polishing business

We need a logo design for a new company out of Toronto, Canada. We polish residential, commercial and industrial concrete as well as different epoxy toppings.

Target Market(s)

How Owners with expendable incomes

Industry/Entity Type

Construction

Contact Information for Business Card

be able to see content rather easily

Colors
0355a3
fbed22
1b1b1b

Requirements
Must have
• simple and elegant

```html
<!DOCTYPE html>
<html lang="en">
<head>
<meta charset="utf-8">
<title>Stonegleam Floors – Business Card</title>
<link rel="stylesheet" href="https://fonts.googleapis.com/css2?family=Play:wght@400;700&family=Lato:wght@400&display=swap">
<style>
  :root {
    --brand-blue: #0355a3;
    --ink: #1b1b1b;
    --card: #ffffff;
    --backdrop: #2b2b2b;
  }
  html, body {
    margin: 0;
    padding: 0;
    width: 1189px;
    height: 1200px;
    overflow: hidden;
    background: var(--backdrop);
  }
  .canvas {
    position: relative;
    width: 1189px;
    height: 1200px;
  }
  .card {
    position: absolute;
    left: 171px;
    width: 857px;
    height: 490px;
    background: var(--card);
    box-shadow: 0 6px 18px rgba(0,0,0,0.45);
  }
  .card--front { top: 66px; }
  .card--back  { top: 625px; }

  .brand {
    position: absolute;
    display: flex;
    align-items: center;
    gap: 14px;
    font-family: 'Play', sans-serif;
    font-weight: 400;
    color: var(--brand-blue);
    white-space: nowrap;
  }
  .brand__square {
    background: var(--brand-blue);
    flex: none;
  }
  .card--front .brand {
    left: 50%;
    top: 50%;
    transform: translate(-50%, -50%);
    font-size: 36px;
  }
  .card--front .brand__square { width: 34px; height: 34px; }

  .card--back .brand {
    left: 207px;
    top: 244px;
    transform: translate(-50%, -50%);
    font-size: 30px;
  }
  .card--back .brand__square { width: 28px; height: 28px; }

  .divider {
    position: absolute;
    left: 408px;
    top: 166px;
    width: 1px;
    height: 156px;
    background: var(--brand-blue);
  }

  .person {
    position: absolute;
    left: 472px;
    top: 160px;
  }
  .person__name {
    margin: 0;
    font-family: 'Play', sans-serif;
    font-weight: 400;
    font-size: 27px;
    line-height: 1;
    color: var(--ink);
  }
  .person__name .surname { color: var(--brand-blue); }
  .person__role {
    margin: 2px 0 0;
    font-family: 'Lato', sans-serif;
    font-size: 19px;
    color: var(--ink);
  }

  .contacts {
    position: absolute;
    left: 472px;
    top: 236px;
    margin: 0;
    padding: 0;
    list-style: none;
    font-family: 'Lato', sans-serif;
    font-size: 19px;
    color: var(--ink);
  }
  .contacts li {
    display: flex;
    align-items: center;
    gap: 8px;
    height: 29px;
  }
  .contacts svg { width: 24px; height: 24px; flex: none; }
</style>
</head>
<body>
<main class="canvas">

  <section class="card card--front" aria-label="Card front">
    <div class="brand">
      <span class="brand__square" aria-hidden="true"></span>
      <span class="brand__name">Stonegleam Floors</span>
    </div>
  </section>

  <section class="card card--back" aria-label="Card back">
    <div class="brand">
      <span class="brand__square" aria-hidden="true"></span>
      <span class="brand__name">Stonegleam Floors</span>
    </div>

    <div class="divider" aria-hidden="true"></div>

    <div class="person">
      <h1 class="person__name">Daniel <span class="surname">Reyes</span></h1>
      <p class="person__role">President</p>
    </div>

    <ul class="contacts">
      <li>
        <svg viewBox="0 0 24 24" aria-hidden="true">
          <circle cx="12" cy="12" r="11" fill="none" stroke="#0355a3" stroke-width="1.5"/>
          <rect x="8.5" y="6" width="7" height="12" rx="1.2" fill="none" stroke="#0355a3" stroke-width="1.5"/>
          <line x1="11" y1="15.8" x2="13" y2="15.8" stroke="#0355a3" stroke-width="1.2"/>
        </svg>
        <span>(416) 555 0142</span>
      </li>
      <li>
        <svg viewBox="0 0 24 24" aria-hidden="true">
          <circle cx="12" cy="12" r="11" fill="none" stroke="#0355a3" stroke-width="1.5"/>
          <rect x="6.5" y="8" width="11" height="8" fill="#0355a3"/>
          <polyline points="6.5,8 12,12.5 17.5,8" fill="none" stroke="#fff" stroke-width="1.1"/>
        </svg>
        <span>info@stonegleamfloors.com</span>
      </li>
      <li>
        <svg viewBox="0 0 24 24" aria-hidden="true">
          <circle cx="12" cy="12" r="11" fill="none" stroke="#0355a3" stroke-width="1.5"/>
          <circle cx="12" cy="12" r="6.5" fill="none" stroke="#0355a3" stroke-width="1.2"/>
          <ellipse cx="12" cy="12" rx="2.8" ry="6.5" fill="none" stroke="#0355a3" stroke-width="1"/>
          <line x1="5.5" y1="12" x2="18.5" y2="12" stroke="#0355a3" stroke-width="1"/>
          <line x1="6.5" y1="9" x2="17.5" y2="9" stroke="#0355a3" stroke-width="0.8"/>
          <line x1="6.5" y1="15" x2="17.5" y2="15" stroke="#0355a3" stroke-width="0.8"/>
        </svg>
        <span>www.stonegleamfloors.com</span>
      </li>
    </ul>
  </section>

</main>
</body>
</html>
```